Children's writer business card design

I write children's mystery and adventure books for 9-12 year olds. My logo is a small robin redbreast bird which I will appear on all my commercial stationery and websites. I have a 'silhouette' of a bird on the mock up on your site and I like this, although your designers might make it look even better. The bird is non-negotiable!

When I tried to do the back of the card I got a hallmark. I don't like this.

I would like the card to be modern, 'clean' and striking. Not too much colour. Definitely the red for the bird so it really stands out.

Target Market(s)

parents and grandparents of children 9-12 years old, booksellers, teachers

Industry/Entity Type

Business

Contact Information for Business Card

I have created a rough design using Cardlyne which I hope you can access as this contains all of the information I want on my card.
The front has the following:
Maren Talbot
Writer & Education Consultant
www.marentalbotwriter.example

04915360284
mtalwex@quillmail.example

The back has:
Books
The Garnet Locket Puzzles (In bold)
The Riddle of the Garnet Locket (in italics)
The Whisper of the Garnet (italics)
The Pomfrey Project (in bold)
Book 1: Stuck (italics)
Book 2: Unstuck (italics)

I'm happy for you to change the design provided the 'robin' stays.
Thank you.

Colors
ec2027

Requirements
Must have
• the robin redbreast bird logo - although it is fine to change how the bird looks.
Should not have
• no watermark

```html
<!DOCTYPE html>
<html lang="en">
<head>
<meta charset="utf-8">
<title>Maren Talbot – Business Card</title>
<link rel="stylesheet" href="https://fonts.googleapis.com/css2?family=Caladea&display=swap">
<style>
  :root {
    --backdrop: #b3a796;
    --pattern-tan: #a99676;
    --pattern-tan-light: #b8a686;
    --band-cream: #ddd3b3;
    --band-cream-light: #e6ddc0;
    --rule-blue: #3f5d7a;
    --text-white: #ffffff;
    --text-outline: #3a2e22;
    --robin-red: #ec2027;
    --robin-black: #1c1a1a;
    --branch-grey: #9a9690;
  }
  * { margin: 0; padding: 0; box-sizing: border-box; }
  html, body { width: 1200px; height: 900px; overflow: hidden; }
  body {
    background: var(--backdrop);
    position: relative;
    font-family: "Caladea", Georgia, serif;
    color: var(--text-white);
  }
  .card {
    position: absolute;
    width: 566px;
    height: 346px;
    overflow: hidden;
    box-shadow: 0 2px 6px rgba(0,0,0,0.25);
  }
  .card--back { left: 447px; top: 100px; }
  .card--front { left: 251px; top: 406px; }

  .card__pattern {
    position: absolute;
    left: 0; top: 0; right: 0;
    background: linear-gradient(180deg, var(--pattern-tan-light), var(--pattern-tan));
  }
  .card--back .card__pattern { height: 268px; }
  .card--front .card__pattern { height: 262px; }

  .card__band {
    position: absolute;
    left: 0; right: 0; bottom: 0;
    background: linear-gradient(180deg, var(--band-cream-light), var(--band-cream));
    border-top: 2px solid var(--rule-blue);
  }
  .card--back .card__band { top: 268px; }
  .card--front .card__band { top: 262px; }

  .outlined {
    color: var(--text-white);
    text-shadow:
      -1px -1px 0 var(--text-outline), 1px -1px 0 var(--text-outline),
      -1px 1px 0 var(--text-outline), 1px 1px 0 var(--text-outline),
      0 0 2px var(--text-outline);
  }

  .book-list {
    position: absolute;
    left: 0; right: 0; top: 44px;
    text-align: center;
    font-size: 25px;
    line-height: 34px;
    padding-left: 40px;
  }
  .book-list__gap { height: 35px; }

  .identity {
    position: absolute;
    left: 0; width: 566px; top: 114px;
    text-align: center;
    font-size: 33px;
    line-height: 34px;
  }
  .identity__name { padding-left: 0; }

  .contact-list {
    position: absolute;
    left: 34px; top: 272px;
    list-style: none;
  }
  .contact-list__item {
    display: flex;
    align-items: center;
    height: 22px;
    font-size: 15px;
  }
  .contact-list__icon {
    width: 36px; height: 20px;
    margin-right: 8px;
  }

  .robin-logo {
    position: absolute;
    left: 409px; top: 189px;
    width: 112px; height: 157px;
  }
</style>
</head>
<body>

  <section class="card card--back" aria-label="Card back: book list">
    <div class="card__pattern" role="img" aria-label="Vintage book-cloth ornamental pattern in muted tan, sage and rose"></div>
    <div class="card__band"></div>
    <div class="book-list outlined">
      <p>Books The Garnet Locket Puzzles</p>
      <p>The Riddle of the Garnet Locket</p>
      <p>The Whisper of the Garnet</p>
      <div class="book-list__gap"></div>
      <p>The Pomfrey Project</p>
      <p>Book 1: Stuck&nbsp;&nbsp;Book 2: Unstuck</p>
    </div>
  </section>

  <section class="card card--front" aria-label="Card front: contact details">
    <div class="card__pattern" role="img" aria-label="Vintage book-cloth ornamental pattern in muted tan, sage and rose"></div>
    <div class="card__band"></div>

    <div class="identity outlined">
      <p class="identity__name">Maren Talbot</p>
      <p class="identity__role">Writer &amp; Education Consultant</p>
    </div>

    <ul class="contact-list outlined">
      <li class="contact-list__item">
        <svg class="contact-list__icon" viewBox="0 0 36 20" aria-hidden="true">
          <rect x="1" y="1" width="34" height="18" rx="5" fill="#fff"/>
          <path d="M11 7 q7 -5 14 0 l-2 2 h-3 v-1 h-4 v1 h-3z M12 10 h12 v6 h-12z" fill="#8a7d68"/>
          <circle cx="18" cy="13" r="2" fill="#fff"/>
        </svg>
        <span>04915360284</span>
      </li>
      <li class="contact-list__item">
        <svg class="contact-list__icon" viewBox="0 0 36 20" aria-hidden="true">
          <rect x="1" y="1" width="34" height="18" rx="5" fill="#fff"/>
          <rect x="8" y="5" width="20" height="10" rx="1" fill="none" stroke="#8a7d68" stroke-width="1.5"/>
          <text x="18" y="12.5" font-size="6" text-anchor="middle" fill="#8a7d68" font-family="Arial, sans-serif">www</text>
        </svg>
        <span>marentalbotwriter.example</span>
      </li>
      <li class="contact-list__item">
        <svg class="contact-list__icon" viewBox="0 0 36 20" aria-hidden="true">
          <rect x="1" y="1" width="34" height="18" rx="5" fill="#fff"/>
          <text x="18" y="15" font-size="14" text-anchor="middle" fill="#8a7d68" font-family="Arial, sans-serif">@</text>
        </svg>
        <span>mtalwex@quillmail.example</span>
      </li>
    </ul>

    <svg class="robin-logo" viewBox="0 0 112 157" role="img" aria-label="Robin redbreast logo perched on a weathered branch">
      <defs>
        <linearGradient id="robin-tones" x1="0" y1="0" x2="0" y2="1">
          <stop offset="0" stop-color="var(--robin-black)"/>
          <stop offset="0.45" stop-color="var(--robin-red)"/>
          <stop offset="0.75" stop-color="var(--robin-red)"/>
          <stop offset="1" stop-color="var(--branch-grey)"/>
        </linearGradient>
      </defs>
      <rect x="0" y="0" width="112" height="157" fill="url(#robin-tones)" opacity="0.9"/>
    </svg>
  </section>

</body>
</html>
```